Brochure design for trade company

I would like to get a professional, easy to read and eye catchy capability statement designed for my electrical business.

My aim is to be able to go to property managers and WOW them when they see the capability statement.

Attached the content writing, design brief, company logo and template of what I like below. If there are any questions please send me a message.

The areas we service photo is an example, please do your own designs for the maps section

Thank you in advance for the help team.

Requirements
Must have
• The areas we service photo is an example, please do your own designs for the maps section
Nice to have
• Eye catching and creative. Also be warm & inviting
Should not have
• Not too out of place looking photos or elements. Don’t make it he design look too cold

```html
<!DOCTYPE html>
<html lang="en">
<head>
<meta charset="utf-8">
<title>Voltline Electrical – Capability Statement</title>
<link href="https://fonts.googleapis.com/css2?family=Roboto:wght@400;500;700;900&family=Open+Sans:wght@400;600;700&display=swap" rel="stylesheet">
<style>
:root{
  --stage:#a3a3a3;
  --orange:#eb9e3c;
  --orange-light:#fbcf9b;
  --ink:#1b1b1b;
  --white:#ffffff;
  --body:#3a3a3a;
  --purple:#8e3fb8;
  --amber:#e08722;
  --pink:#ea3a78;
  --violet:#6a47b8;
  --ring:#d9dde4;
}
*{box-sizing:border-box;margin:0;padding:0}
html,body{width:692px;height:1200px;overflow:hidden;background:var(--stage)}
body{position:relative;font-family:"Open Sans",sans-serif;color:var(--ink)}
.page{position:absolute;width:241px;height:341px;background:var(--white);overflow:hidden;box-shadow:4px 6px 8px rgba(0,0,0,.35)}
.page--cover{left:63px;top:43px}
.page--about{left:384px;top:43px}
.page--areas{left:63px;top:430px}
.page--services{left:384px;top:430px}
.page--contact{left:63px;top:816px}
.abs{position:absolute}
.brand{position:absolute;background:#0d0d0d;color:var(--white);font-family:"Roboto",sans-serif;font-weight:900;display:flex;align-items:center;justify-content:center;text-align:center;line-height:1;letter-spacing:1px;white-space:nowrap}
.heading{font-family:"Roboto",sans-serif;font-weight:900;font-size:11px;line-height:1.1;color:var(--ink)}
.heading em{font-style:normal;color:var(--orange)}
.footer{position:absolute;left:0;bottom:0;width:100%;height:14px;background:var(--orange);color:var(--white);font-size:6px;font-weight:600;display:flex;align-items:center;justify-content:center;gap:6px}
.photo{position:absolute}

/* cover */
.cover-photo{left:0;top:0;width:241px;height:341px;
  background:
    radial-gradient(ellipse 70% 18% at 62% 44%,rgba(255,214,110,.95),rgba(255,170,50,0) 70%),
    linear-gradient(180deg,#3f5f92 0%,#7d7a98 14%,#d9905a 26%,#f6a83a 38%,#f08a22 46%,#b9562a 53%,#4d3a3c 60%,#231d1f 72%,#121212 100%)}
.cover-title{position:absolute;left:0;width:100%;top:239px;text-align:center;color:var(--white);font-family:"Roboto",sans-serif;font-weight:900;font-size:35px;line-height:.9;letter-spacing:.5px}
.cover-tag{position:absolute;left:0;width:100%;top:301px;text-align:center;color:var(--white);font-family:"Roboto",sans-serif;font-weight:700;font-size:8px}
.cover-sectors{position:absolute;left:0;width:100%;top:323px;text-align:center;color:var(--white);font-family:"Roboto",sans-serif;font-weight:700;font-size:8.3px}

/* about */
.about-photo{left:132px;top:-8px;width:136px;height:136px;border-radius:50%;border:4px solid var(--orange-light);
  background:
    radial-gradient(circle at 58% 40%,#f08a2c 0,#e6823a 9%,rgba(230,130,58,0) 22%),
    radial-gradient(circle at 45% 50%,#e7b48f 0,#c98d6a 20%,rgba(200,140,105,0) 40%),
    linear-gradient(135deg,#4a4f5c 0%,#7b7f88 35%,#c9c9cc 65%,#e5e4e2 100%)}
.about-title{left:19px;top:53px;font-size:11px;color:var(--ink)}
.about-title span{color:var(--white)}
.about-text{left:19px;top:152px;width:200px;font-size:5.9px;line-height:9px;color:var(--body)}
.about-text p{margin-bottom:5px}
.values{left:0;top:253px;width:100%;text-align:center}
.values .heading{display:inline-block;border-bottom:.6px solid var(--orange);padding-bottom:1px}
.value{position:absolute;top:273px;width:48px;height:48px;border-radius:50%;border:3px solid var(--ring);display:flex;align-items:center;justify-content:center;text-align:center;color:var(--white);font-family:"Roboto",sans-serif;font-weight:700;font-size:4.2px;line-height:1.15;padding:6px;box-shadow:inset 0 0 0 3px rgba(255,255,255,.25)}
.value--reliability{left:13px;background:linear-gradient(160deg,#a34cc4,var(--purple))}
.value--community{left:69px;background:linear-gradient(160deg,#f0a04a,var(--amber))}
.value--customer{left:125px;background:linear-gradient(160deg,#f2689a,var(--pink))}
.value--openness{left:181px;background:linear-gradient(160deg,#8a5bd0,var(--violet))}

/* lists */
.ticks{list-style:none}
.ticks li{position:relative;padding-left:17px}
.ticks li::before{content:"✓";position:absolute;left:1px;top:1px;width:8px;height:8px;border:1px solid var(--orange);border-radius:50%;color:var(--orange);font-size:7px;line-height:6px;text-align:center;font-weight:700}
.promise{left:17px;top:136px;width:214px;font-size:5.9px;line-height:9px;color:var(--body)}
.promise li{margin-bottom:3px}
.service-list{left:17px;top:121px;width:215px;font-family:"Roboto",sans-serif;font-weight:400;font-size:8px;line-height:10.5px;color:var(--ink)}
.service-list li{margin-bottom:3.6px}

/* areas */
.map{left:16px;top:16px;width:91px;height:88px;box-shadow:1px 2px 4px rgba(0,0,0,.3);
  background:
    radial-gradient(ellipse 30% 40% at 90% 70%,#9cc7e8 0,#b8d6ee 50%,rgba(184,214,238,0) 100%),
    radial-gradient(ellipse 40% 30% at 30% 25%,#cfe3c8 0,rgba(207,227,200,0) 100%),
    linear-gradient(135deg,#f1f3ef 0%,#e3ebe0 45%,#d6e6d4 70%,#c4dbe9 100%)}
.board-photo{left:19px;top:208px;width:204px;height:107px;border-radius:5px;
  background:
    radial-gradient(ellipse 25% 35% at 82% 25%,#f3f3f3 0,rgba(243,243,243,0) 100%),
    radial-gradient(ellipse 30% 40% at 78% 78%,#5b6b80 0,rgba(91,107,128,0) 100%),
    linear-gradient(90deg,#5d5a55 0%,#8a8782 14%,#d8dadb 32%,#eceeee 50%,#c3c8cc 68%,#9aa2aa 100%)}

/* services */
.cables-photo{left:124px;top:-14px;width:122px;height:102px;border-radius:50%;border:4px solid var(--orange-light);
  background:
    radial-gradient(ellipse 35% 30% at 35% 30%,#3f7bd0 0,rgba(63,123,208,0) 100%),
    radial-gradient(ellipse 30% 30% at 75% 30%,#f2f2f2 0,rgba(242,242,242,0) 100%),
    radial-gradient(ellipse 45% 35% at 65% 85%,#b3453b 0,rgba(179,69,59,0) 100%),
    linear-gradient(160deg,#e9e9ea 0%,#c9cdd2 50%,#7f8891 100%)}

/* contact */
.contact-block{left:0;top:135px;width:100%;text-align:center;font-family:"Roboto",sans-serif}
.contact-line{font-size:7.4px;font-weight:700;line-height:13.5px}
.contact-line em{font-style:normal;font-weight:500;color:var(--orange)}
.review-name{left:0;top:240px;width:100%;text-align:center;font-family:"Roboto",sans-serif;font-weight:700;font-size:26px;color:#4a7fd8}
.review-stars{left:0;top:272px;width:100%;text-align:center;font-family:"Roboto",sans-serif;font-weight:700;font-size:9px;color:var(--ink)}
.review-stars span{color:#f2b21c;letter-spacing:-.5px}
.logo-sheet{left:346px;top:916px;width:293px;height:83px;font-size:25px;letter-spacing:1.5px}
</style>
</head>
<body>

<section class="page page--cover">
  <div class="photo cover-photo" role="img" aria-label="Silhouette of a line worker beside power poles against a sunset sky"></div>
  <div class="brand" style="left:147px;top:12px;width:82px;height:23px;font-size:8px">VOLTLINE</div>
  <h1 class="cover-title">CAPABILITY<br>STATEMENT</h1>
  <p class="cover-tag">WHEN QUALITY AND RELIABILITY COUNTS</p>
  <p class="cover-sectors">RESIDENTIAL | COMMERCIAL | REAL ESTATE | STRATA</p>
</section>

<section class="page page--about">
  <svg class="abs" style="left:0;top:0" width="241" height="160" viewBox="0 0 241 160">
    <path d="M0 0H241V160C200 160 160 140 140 110C120 80 95 95 70 105C40 117 15 108 0 112Z" fill="var(--orange-light)"/>
    <path d="M0 0H241V150C200 150 160 130 140 100C120 72 95 88 70 98C40 108 15 100 0 104Z" fill="var(--orange)"/>
  </svg>
  <div class="photo about-photo" role="img" aria-label="Hands testing a wall power point with a multimeter"></div>
  <div class="brand" style="left:20px;top:22px;width:82px;height:23px;font-size:8px">VOLTLINE</div>
  <h2 class="heading abs about-title">ABOUT VOLTLINE<br><span>ELECTRICAL</span></h2>
  <h3 class="heading abs" style="left:19px;top:134px">WHO WE <em>ARE</em></h3>
  <div class="abs about-text">
    <p>Voltline Electrical, we’re more than just a team<br>of electricians—we’re your extended family that you can<br>rely on 24/7 for reliable, expert help for anything electrical related.</p>
    <p>With our friendly, reliable, and no-nonsense approach, we ensure<br>that your needs are met with professionalism and a smile.<br>Whether it’s a small repair or a major installation, we’re here to make your life easier.</p>
    <p>At Voltline Electrical, we make sure that every job counts.</p>
  </div>
  <div class="abs values"><h3 class="heading">CORE <em>VALUES</em></h3></div>
  <div class="value value--reliability">RELIABILITY AND SAFETY FIRST</div>
  <div class="value value--community">COMMUNITY AND RESPECT</div>
  <div class="value value--customer">CUSTOMER FOCUSED</div>
  <div class="value value--openness">OPENNESS, TRUST AND ACCOUNTABILITY</div>
  <footer class="footer"><span>Company ABN: 12 345 678 901</span><span>|</span><span>www.VoltlineElectrical.com.au</span></footer>
</section>

<section class="page page--areas">
  <svg class="abs" style="left:0;top:0" width="241" height="110" viewBox="0 0 241 110">
    <path d="M0 0H155C150 20 130 30 110 32C80 36 60 50 50 75C42 95 20 105 0 108Z" fill="var(--orange)"/>
  </svg>
  <div class="photo map" role="img" aria-label="Map of the metropolitan service area"></div>
  <div class="brand" style="left:135px;top:29px;width:90px;height:25px;font-size:8.5px">VOLTLINE</div>
  <h2 class="heading abs" style="right:17px;top:80px;border-bottom:.6px solid var(--orange);padding-bottom:2px">AREAS WE <em>SERVICE</em></h2>
  <h3 class="heading abs" style="left:17px;top:117px">OUR PROMISE <em>TO YOU</em></h3>
  <ul class="ticks abs promise">
    <li>Around clock communication. We can always be reached 24/7</li>
    <li>Service with a smile on our face. We take the stress out of daily life and let you do the things you want to do</li>
    <li>Reliability and speed, quotations and WO’s actioned promptly</li>
    <li>All our staff are trained to the highest level with expert knowledge in the industry to make a tailored solution for clients</li>
  </ul>
  <div class="photo board-photo" role="img" aria-label="Electrician in a hard hat checking a switchboard with a tablet"></div>
  <footer class="footer"><span>Company ABN: 12 345 678 901</span><span>|</span><span>www.VoltlineElectrical.com.au</span></footer>
</section>

<section class="page page--services">
  <svg class="abs" style="left:0;top:0" width="241" height="100" viewBox="0 0 241 100">
    <path d="M0 0H241V95C200 95 165 80 140 70C110 58 90 75 60 70C30 66 15 70 0 75Z" fill="var(--orange-light)"/>
    <path d="M0 0H150C140 18 110 22 80 20C45 18 20 30 0 45Z" fill="var(--orange)"/>
  </svg>
  <div class="photo cables-photo" role="img" aria-label="Electrician in a hard hat sorting coloured cables"></div>
  <div class="brand" style="left:17px;top:34px;width:89px;height:26px;font-size:8.5px">VOLTLINE</div>
  <h2 class="heading abs" style="left:18px;top:99px">OUR MAINTENANCE <em>SERVICES</em></h2>
  <ul class="ticks abs service-list">
    <li>24/7 Emergency services</li>
    <li>Fault finding and diagnostics</li>
    <li>Switchboard upgrade and repairs</li>
    <li>General lighting installations &amp; repairs</li>
    <li>PowerPoint installation</li>
    <li>Electric storage hot water systems service</li>
    <li>Smoke alarm installation and compliance</li>
    <li>Appliance repair/ installations</li>
    <li>Ventiatlion &amp; mould prevention – ceiling fans,<br>exhaust fans, underfloor ventilation</li>
    <li>TV,Data and antenna services</li>
    <li>Surge protection</li>
    <li>EV charging systems and lighting upgrades for<br>commercial premises</li>
  </ul>
  <footer class="footer"><span>Company ABN: 12 345 678 901</span><span>|</span><span>www.VoltlineElectrical.com.au</span></footer>
</section>

<section class="page page--contact">
  <svg class="abs" style="left:0;top:0" width="241" height="110" viewBox="0 0 241 110">
    <path d="M0 0H241V40C215 30 195 30 170 45C140 62 120 60 110 60C70 62 70 100 30 100C15 100 5 98 0 96Z" fill="var(--orange-light)"/>
    <path d="M0 0H150C150 18 130 30 105 30C70 30 55 45 55 60C55 85 30 100 0 100Z" fill="var(--orange)"/>
  </svg>
  <div class="brand" style="left:70px;top:90px;width:97px;height:27px;font-size:9.5px">VOLTLINE</div>
  <div class="abs contact-block">
    <h2 class="heading" style="margin-bottom:4px">CONTACT</h2>
    <p class="contact-line">Daniel Reyes – <em>Director 0400 123 456</em></p>
    <p class="contact-line">Company ABN : <em>12 345 678 901</em></p>
    <p class="contact-line">Website : <em>Voltlineelectrical.com.au</em></p>
    <p class="contact-line">Hello@Voltlineelectrical<em>.com.au</em></p>
    <p class="contact-line">Electrical Supervisors Licence : <em>100000C</em></p>
  </div>
  <p class="abs review-name">Rateline</p>
  <p class="abs review-stars"><span>★★★★★</span> REVIEW!</p>
  <div class="abs" style="left:0;bottom:0;width:100%;height:6px;background:var(--orange)"></div>
</section>

<div class="brand logo-sheet">VOLTLINE ELECTRICAL</div>

</body>
</html>
```